Website Design for Kindred Harbor Network

Please design and code a new website.
Here are the sites I like best:
http://www.voyaglint.com/alternate/
http://www.wheelsbrevant.org
Please make it similar but look at the competitor site (below) for images and wording. This is NOT a car donation site. It's a senior lead placement site like https://www.elderbrookhaven.com. I just like this sites above as a lead generation sites.
Competitor site:
https://www.elderbrookhaven.com (use ideas / verbiage from this site)
Updates
Competitor site:

```html
<!DOCTYPE html>
<html lang="en">
<head>
<meta charset="utf-8">
<title>Kindred Harbor Network – Senior Living Advisors</title>
<link href="https://fonts.googleapis.com/css2?family=Exo:wght@400;500&family=Montserrat:ital,wght@0,400;0,500;0,600;1,400&display=swap" rel="stylesheet">
<style>
:root{
  --red:#e8392e;
  --navy:#0d2a8c;
  --ink:#222;
  --muted:#555;
  --grey-bg:#f1f2f4;
  --line:#c9c9c9;
  --white:#fff;
  --black:#000;
}
*{box-sizing:border-box;margin:0;padding:0}
html,body{width:1200px;height:2904px;overflow:hidden;background:var(--white)}
body{font-family:"Montserrat",sans-serif;color:var(--ink)}
.canvas{position:relative;width:1200px;height:2904px;overflow:hidden}
.abs{position:absolute}
h2{font-family:"Exo",sans-serif;font-weight:400;color:var(--navy);font-size:30px;text-align:center;letter-spacing:.3px}
h2 em{font-style:normal;color:var(--red)}
.divider{position:absolute;left:564px;width:72px;height:3px;display:flex;gap:4px}
.divider span{flex:1;background:var(--navy)}
.divider span+span{background:var(--red)}
.lead{font-size:12px;line-height:19px;text-align:center;color:var(--ink)}

/* header */
.brand{left:141px;top:16px}
.brand-name{font-family:"Exo",sans-serif;font-size:25px;color:var(--navy);font-weight:400}
.brand-sub{display:flex;align-items:center;gap:10px;font-size:11px;color:var(--red);margin-top:4px}
.brand-sub i{display:block;width:22px;height:1px;background:var(--ink)}
.navbar{left:0;top:83px;width:1200px;height:35px;background:var(--navy)}
.nav a{position:absolute;top:0;height:35px;line-height:35px;color:var(--white);font-size:12px;font-weight:500;text-decoration:none;padding:0 18px}
.nav a.active{background:var(--red)}
.caret{display:inline-block;border:4px solid transparent;border-top:5px solid currentColor;margin-left:8px;vertical-align:-2px}

.hero{left:0;top:118px;width:1200px;height:353px;background:linear-gradient(100deg,#cfc9bf 0%,#e3ddd3 30%,#b9b3a8 55%,#8d9a7c 75%,#5f7a4c 100%)}

.lead-box{left:748px;top:0;width:282px;height:471px;background:var(--red)}
.help{left:0;top:18px;width:100%;display:flex;align-items:center;gap:10px;padding-left:22px;color:var(--white)}
.help-text{font-family:"Exo",sans-serif;line-height:21px}
.help-text small{display:block;font-size:17px}
.help-text b{display:block;font-size:21px;font-weight:400}
.lang{position:absolute;left:207px;top:4px;width:57px;height:34px;border:1px solid rgba(255,255,255,.7);display:flex;align-items:center;justify-content:center;gap:6px}
.lang i{display:block;width:20px;height:13px;background:var(--white)}
.ribbon{left:-4px;top:80px;width:290px;height:37px;background:var(--white);font-size:13px;color:var(--ink);text-align:center;line-height:37px;clip-path:polygon(0 0,100% 0,96% 50%,100% 100%,0 100%,4% 50%)}
.form-title{left:0;top:140px;width:100%;text-align:center;color:var(--white);font-size:13px;font-weight:500}
.field{position:absolute;height:25px;background:var(--white);border-radius:2px;font-size:10px;color:var(--muted);line-height:25px;padding-left:10px}
.field .caret{position:absolute;right:10px;top:8px;margin:0;color:var(--ink)}
.btn-search{left:25px;top:380px;width:232px;height:35px;border-radius:18px;background:var(--navy);color:var(--white);font-family:"Exo",sans-serif;font-size:16px;text-align:center;line-height:35px}

/* features */
.features{left:141px;top:664px;width:918px;display:flex;justify-content:space-between}
.feature{width:160px;text-align:center;font-size:13px;font-weight:600;line-height:18px;color:var(--ink)}
.feature-icon{width:118px;height:118px;margin:0 auto 16px;border-radius:50%;border:3px solid var(--navy);padding:3px;background:var(--white)}
.feature-icon div{width:100%;height:100%;border-radius:50%;background:var(--red);display:flex;align-items:center;justify-content:center}

/* cost band */
.cost{left:0;top:908px;width:1200px;height:353px;background:linear-gradient(90deg,#3f4530 0%,#6b6440 35%,#9a8a64 60%,#c4bca8 80%,#8c8778 100%)}
.cost-shade{left:0;top:908px;width:1200px;height:353px;background:rgba(20,20,20,.45)}
.cost-title{left:0;top:972px;width:1200px;color:var(--white)}
.cost-title em{color:var(--red)}
.cost-text{left:420px;top:1042px;width:360px;color:#eee;font-size:13px;line-height:19px;text-align:center;letter-spacing:.3px}
.cost-call{left:0;top:1109px;width:1200px;display:flex;justify-content:center;align-items:center;gap:10px;color:var(--white);font-family:"Exo",sans-serif;font-size:21px}
.btn-contact{left:509px;top:1155px;width:182px;height:34px;border-radius:17px;background:var(--navy);color:var(--white);font-family:"Exo",sans-serif;font-size:16px;display:flex;align-items:center;justify-content:center;gap:14px}

/* advisor */
.cards{left:141px;top:1450px;width:918px;display:flex;justify-content:space-between}
.card{width:284px;height:107px;border:1px solid #bbb;border-radius:3px;position:relative;padding:14px 14px 0 71px}
.card svg{position:absolute;left:14px;top:14px}
.card h3{font-family:"Exo",sans-serif;font-weight:400;font-size:15px;line-height:20px;color:var(--ink)}
.card p{font-size:11px;line-height:17px;color:var(--muted);margin-top:10px}
.finder{left:353px;top:1599px;width:494px;height:35px;display:flex}
.finder-input{flex:0 0 247px;border:1px solid #999;border-right:0;border-radius:18px 0 0 18px;font-size:14px;color:#888;line-height:33px;padding-left:41px}
.finder-btn{flex:1;background:var(--navy);color:var(--white);border-radius:0 18px 18px 0;font-family:"Exo",sans-serif;font-size:17px;line-height:35px;text-align:center}

/* testimonials */
.reviews{left:0;top:1703px;width:1200px;height:426px;background:var(--grey-bg)}
.quote{left:0;top:1848px;width:1200px;text-align:center;font-style:italic;font-size:13px;color:var(--muted)}
.reviewer{left:0;top:1882px;width:1200px;text-align:center;font-size:12px;font-weight:600;color:#444}
.reviewer-note{left:0;top:1909px;width:1200px;text-align:center;font-size:9px;color:#666}
.avatar{position:absolute;top:1945px;width:74px;height:74px;border-radius:10px}
.avatar.current{border:4px solid var(--red)}
.dots{left:580px;top:2049px;display:flex;gap:6px}
.dots i{display:block;width:8px;height:8px;border-radius:50%;background:#c8c8c8}
.dots i:first-child{background:var(--red)}

/* states */
.states{left:140px;top:2286px;width:920px;height:386px;background:var(--white);box-shadow:0 0 10px rgba(0,0,0,.12);border-radius:4px}
.tabs{position:absolute;left:0;top:0;width:100%;height:52px;display:flex;background:var(--white);box-shadow:0 4px 6px rgba(0,0,0,.08)}
.tab{font-family:"Montserrat",sans-serif;font-size:13px;font-weight:500;line-height:17px;text-align:center;padding-top:9px;color:var(--ink)}
.tab.active{color:var(--red);background:var(--white);box-shadow:0 -2px 6px rgba(0,0,0,.1);border-radius:4px 4px 0 0;position:relative;z-index:1}
.state-col{position:absolute;top:82px;list-style:none;font-size:12px;line-height:17px;color:#333}

/* footer */
.footer{left:0;top:2743px;width:1200px;height:128px;background:var(--black)}
.footer-nav a{position:absolute;top:2762px;color:var(--white);font-size:12px;font-weight:500;text-decoration:none}
.footer-rule{left:141px;top:2797px;width:671px;height:1px;background:#333}
.contact{position:absolute;top:2818px;display:flex;gap:10px;color:var(--white);font-size:12px;line-height:16px}
.contact b{display:block;font-weight:600}
.contact-icon{flex:0 0 26px;height:26px;border:1px solid var(--white);border-radius:50%;margin-top:6px;display:flex;align-items:center;justify-content:center}
.footer-brand{left:812px;top:2777px;width:248px;text-align:right;color:var(--white)}
.footer-brand .brand-name{color:var(--white);font-size:22px}
.footer-brand .brand-sub{color:var(--white);justify-content:flex-end}
.footer-brand .brand-sub i{background:var(--white)}
.copy{left:0;top:2871px;width:1200px;height:33px;background:var(--red)}
.copy p{position:absolute;left:141px;top:10px;font-size:11px;color:var(--white)}
.social{position:absolute;top:4px;width:26px;height:26px;border:1.5px solid var(--white);border-radius:50%}
</style>
</head>
<body>
<div class="canvas">

  <!-- header -->
  <div class="abs brand">
    <div class="brand-name">Kindred Harbor Network</div>
    <div class="brand-sub"><i></i>Seniorcare Nonprofit<i></i></div>
  </div>

  <div class="abs hero" role="img" aria-label="Photo of a smiling elderly couple touching foreheads outdoors"></div>

  <div class="abs navbar">
    <nav class="nav">
      <a class="active" style="left:141px;width:127px">Assisted Living</a>
      <a style="left:278px">Memory Care</a>
      <a style="left:414px">Nursing Homes</a>
      <a style="left:567px">More Living Options<span class="caret"></span></a>
    </nav>
  </div>

  <div class="abs lead-box">
    <div class="abs help">
      <svg width="20" height="20" viewBox="0 0 24 24"><path fill="#fff" d="M6.6 10.8c1.4 2.8 3.8 5.1 6.6 6.6l2.2-2.2c.3-.3.7-.4 1-.2 1.1.4 2.3.6 3.6.6.6 0 1 .4 1 1V20c0 .6-.4 1-1 1C10.6 21 3 13.4 3 4c0-.6.4-1 1-1h3.5c.6 0 1 .4 1 1 0 1.3.2 2.5.6 3.6.1.3 0 .7-.2 1z"/></svg>
      <div class="help-text"><small>Need help? Call</small><b>800-555-0142</b></div>
      <div class="lang"><i></i><span class="caret" style="color:#fff;margin:4px 0 0"></span></div>
    </div>
    <div class="abs ribbon">Talk to a local advisor for FREE</div>
    <div class="abs form-title">Find Senior Living Near You.</div>
    <div class="field" style="left:25px;top:175px;width:106px">Firest Name</div>
    <div class="field" style="left:151px;top:175px;width:106px">Last Name</div>
    <div class="field" style="left:25px;top:215px;width:232px">Phone Number</div>
    <div class="field" style="left:25px;top:254px;width:232px">Email Address</div>
    <div class="field" style="left:25px;top:294px;width:106px">Select State<span class="caret"></span></div>
    <div class="field" style="left:151px;top:294px;width:106px">select City<span class="caret"></span></div>
    <div class="field" style="left:25px;top:333px;width:232px">Zip Code</div>
    <div class="abs btn-search">Start Your Search</div>
  </div>

  <!-- support -->
  <h2 class="abs" style="left:0;top:535px;width:1200px">The support you need to make the <em>RIGHT CHOICE</em></h2>
  <div class="divider" style="top:583px"><span></span><span></span></div>
  <p class="abs lead" style="left:380px;top:603px;width:440px">Elderbrook Haven has already helped thousands of families find peace of mind. Here’s what’s included with our free service:</p>

  <div class="abs features">
    <div class="feature"><div class="feature-icon"><div>
      <svg width="50" height="54" viewBox="0 0 50 54"><circle cx="25" cy="15" r="13" fill="#fff"/><path d="M2 52c0-14 10-22 23-22s23 8 23 22z" fill="#fff"/></svg>
    </div></div>Dedicated local advisor</div>
    <div class="feature"><div class="feature-icon"><div>
      <svg width="56" height="48" viewBox="0 0 56 48"><path d="M28 2 2 26h8v20h14V32h8v14h14V26h8z" fill="#fff"/></svg>
    </div></div>Hand-picked list of communities to match your needs</div>
    <div class="feature"><div class="feature-icon"><div>
      <svg width="34" height="56" viewBox="0 0 34 56"><text x="17" y="48" text-anchor="middle" font-family="Montserrat,sans-serif" font-size="56" font-weight="600" fill="#fff">$</text></svg>
    </div></div>Full details and pricing</div>
    <div class="feature"><div class="feature-icon"><div>
      <svg width="50" height="50" viewBox="0 0 50 50"><rect x="2" y="6" width="46" height="42" rx="3" fill="#fff"/><rect x="10" y="1" width="5" height="10" fill="#fff"/><rect x="35" y="1" width="5" height="10" fill="#fff"/><g fill="#e8392e"><rect x="7" y="18" width="7" height="6"/><rect x="17" y="18" width="7" height="6"/><rect x="27" y="18" width="7" height="6"/><rect x="37" y="18" width="7" height="6"/><rect x="7" y="27" width="7" height="6"/><rect x="17" y="27" width="7" height="6"/><rect x="27" y="27" width="7" height="6"/><rect x="37" y="27" width="7" height="6"/><rect x="7" y="36" width="7" height="6"/><rect x="17" y="36" width="7" height="6"/><rect x="27" y="36" width="7" height="6"/><rect x="37" y="36" width="7" height="6"/></g></svg>
    </div></div>Help scheduling tours</div>
    <div class="feature"><div class="feature-icon"><div>
      <svg width="60" height="44" viewBox="0 0 60 44"><path d="M2 14h14l-3 0 0 0H2zM4 12l10-10h5v28H4z" fill="#fff"/><rect x="20" y="2" width="38" height="28" rx="2" fill="#fff"/><rect x="2" y="28" width="56" height="6" fill="#fff"/><circle cx="14" cy="36" r="6" fill="#fff" stroke="#e8392e" stroke-width="3"/><circle cx="46" cy="36" r="6" fill="#fff" stroke="#e8392e" stroke-width="3"/></svg>
    </div></div>Move in support</div>
  </div>

  <!-- cost band -->
  <div class="abs cost" role="img" aria-label="Photo of a caregiver chatting with a smiling elderly woman outdoors"></div>
  <div class="abs cost-shade"></div>
  <h2 class="abs cost-title">There’s no <em>cost</em> to you.</h2>
  <div class="divider" style="top:1020px"><span style="background:#fff"></span><span></span></div>
  <p class="abs cost-text">We work with over 20,000 senior living communities. Our community partners pay us for placement services.</p>
  <div class="abs cost-call">
    <svg width="20" height="20" viewBox="0 0 24 24"><path fill="#fff" d="M6.6 10.8c1.4 2.8 3.8 5.1 6.6 6.6l2.2-2.2c.3-.3.7-.4 1-.2 1.1.4 2.3.6 3.6.6.6 0 1 .4 1 1V20c0 .6-.4 1-1 1C10.6 21 3 13.4 3 4c0-.6.4-1 1-1h3.5c.6 0 1 .4 1 1 0 1.3.2 2.5.6 3.6.1.3 0 .7-.2 1z"/></svg>
    Call800-555-0142
  </div>
  <div class="abs btn-contact">Contact Now
    <svg width="18" height="16" viewBox="0 0 18 16"><path d="M0 7 18 0l-4 16-5-5-3 4V10l9-8-11 7z" fill="#fff"/></svg>
  </div>

  <!-- advisor -->
  <h2 class="abs" style="left:0;top:1324px;width:1200px">Your <em>LOCAL ADVISOR</em> informs. You decide.</h2>
  <div class="divider" style="top:1373px"><span></span><span></span></div>
  <p class="abs lead" style="left:0;top:1393px;width:1200px;font-size:11px">Over 400 senior advisors across the U.S. and Canada are ready to help your family with:</p>

  <div class="abs cards">
    <div class="card">
      <svg width="30" height="58" viewBox="0 0 30 58"><circle cx="15" cy="13" r="11" fill="none" stroke="#e8392e" stroke-width="2"/><circle cx="11" cy="11" r="3" fill="#e8392e"/><line x1="15" y1="24" x2="15" y2="56" stroke="#e8392e" stroke-width="2"/></svg>
      <h3>Insider’s tips for the area near you</h3>
      <p>Lorem ipsum dolor sit amet, consectetur adipiscing elit.</p>
    </div>
    <div class="card">
      <svg width="46" height="42" viewBox="0 0 46 42"><path d="M23 40 5 22C-1 16 1 5 10 3c6-1 10 2 13 7 3-5 7-8 13-7 9 2 11 13 5 19z" fill="none" stroke="#e8392e" stroke-width="2"/></svg>
      <h3>Advice tailored to your unique situation</h3>
      <p>Lorem ipsum dolor sit amet, consectetur adipiscing elit.</p>
    </div>
    <div class="card">
      <svg width="44" height="44" viewBox="0 0 44 44"><circle cx="22" cy="22" r="20" fill="none" stroke="#e8392e" stroke-width="2"/><path d="M22 8v15H10" fill="none" stroke="#e8392e" stroke-width="2"/></svg>
      <h3>Time saving know-how and resources</h3>
      <p>Lorem ipsum dolor sit amet, consectetur adipiscing elit.</p>
    </div>
  </div>

  <div class="abs finder">
    <div class="finder-input">Enter city or postal code</div>
    <div class="finder-btn">Find An Advisor Near You</div>
  </div>

  <!-- testimonials -->
  <div class="abs reviews"></div>
  <h2 class="abs" style="left:0;top:1769px;width:1200px"><em>97%</em> of our customers recommend our service</h2>
  <div class="divider" style="top:1817px"><span></span><span></span></div>
  <p class="abs quote">“You were a great help. We really appreciate you &amp; Elderbrook Haven!”</p>
  <p class="abs reviewer">DALE M</p>
  <p class="abs reviewer-note">Looking for Senior Living for his wife in Denver, CO</p>
  <div class="avatar" style="left:455px;background:linear-gradient(#e4e4e4,#c9c6c2)" role="img" aria-label="Portrait photo of an older man"></div>
  <div class="avatar current" style="left:563px;background:linear-gradient(#8fc0dc,#d8b79a)" role="img" aria-label="Photo of an elderly couple at the beach"></div>
  <div class="avatar" style="left:671px;background:linear-gradient(#f3f3f3,#cfe3e3)" role="img" aria-label="Portrait photo of a smiling older woman"></div>
  <div class="abs dots"><i></i><i></i><i></i></div>

  <!-- states -->
  <h2 class="abs" style="left:0;top:2193px;width:1200px">Senior Living by <em>State</em></h2>
  <div class="divider" style="top:2241px"><span></span><span></span></div>

  <div class="abs states">
    <div class="tabs">
      <div class="tab" style="width:105px;padding-left:8px">Memory<br>Care</div>
      <div class="tab active" style="width:153px">Assisted<br>Living</div>
      <div class="tab" style="width:148px">Independent<br>Living</div>
      <div class="tab" style="width:110px">Nursing<br>Home</div>
      <div class="tab" style="width:120px">Care<br>Homes</div>
    </div>
    <ul class="state-col" style="left:24px">
      <li>Alabama</li><li>Arizona</li><li>Arkansas</li><li>California</li><li>Colorado</li><li>Connecticut</li><li>Delaware</li><li>District of Columbia</li><li>Florida</li><li>Georgia</li><li>Hawaii</li><li>Idaho</li><li>Illinois</li><li>Indiana</li><li>Iowa</li><li>Kansas</li><li>Kentucky</li>
    </ul>
    <ul class="state-col" style="left:324px">
      <li>Louisiana</li><li>Maine</li><li>Maryland</li><li>Massachusetts</li><li>Michigan</li><li>Minnesota</li><li>Mississippi</li><li>Missouri</li><li>Montana</li><li>Nebraska</li><li>Nevada</li><li>New Hampshire</li><li>New Jersey</li><li>New Mexico</li><li>New York</li><li>North Carolina</li><li>North Dakota</li>
    </ul>
    <ul class="state-col" style="left:648px">
      <li>Ohio</li><li>Oklahoma</li><li>Oregon</li><li>Pennsylvania</li><li>Rhode Island</li><li>South Carolina</li><li>South Dakota</li><li>Tennessee</li><li>Texas</li><li>Utah</li><li>Vermont</li><li>Virginia</li><li>Washington</li><li>West Virginia</li><li>Wisconsin</li><li>Wyoming</li>
    </ul>
  </div>

  <!-- footer -->
  <footer>
    <div class="abs footer"></div>
    <nav class="footer-nav">
      <a style="left:142px">Assisted Living</a>
      <a style="left:279px">Memory Care</a>
      <a style="left:415px">Nursing Homes</a>
      <a style="left:567px">More Living Options<span class="caret"></span></a>
    </nav>
    <div class="abs footer-rule"></div>
    <div class="contact" style="left:182px;width:280px">
      <span class="contact-icon"><svg width="10" height="14" viewBox="0 0 10 14"><path d="M5 0a5 5 0 0 0-5 5c0 4 5 9 5 9s5-5 5-9a5 5 0 0 0-5-5zm0 7a2 2 0 1 1 0-4 2 2 0 0 1 0 4z" fill="#2a4fd6"/></svg></span>
      <div><b>Address</b>48 Harbor Lane, Suite 210, Portland, ME 04101</div>
    </div>
    <div class="contact" style="left:470px">
      <span class="contact-icon"><svg width="12" height="12" viewBox="0 0 24 24"><path fill="#2a4fd6" d="M6.6 10.8c1.4 2.8 3.8 5.1 6.6 6.6l2.2-2.2c.3-.3.7-.4 1-.2 1.1.4 2.3.6 3.6.6.6 0 1 .4 1 1V20c0 .6-.4 1-1 1C10.6 21 3 13.4 3 4c0-.6.4-1 1-1h3.5c.6 0 1 .4 1 1 0 1.3.2 2.5.6 3.6.1.3 0 .7-.2 1z"/></svg></span>
      <div><b>Call Us :</b>800-555-0142</div>
    </div>
    <div class="contact" style="left:616px">
      <span class="contact-icon"><svg width="12" height="9" viewBox="0 0 12 9"><rect width="12" height="9" rx="1" fill="#2a4fd6"/></svg></span>
      <div><b>Email Us :</b>info@kindredharbor.org</div>
    </div>
    <div class="abs footer-brand">
      <div class="brand-name">Kindred Harbor Network</div>
      <div class="brand-sub"><i></i>Seniorcare Nonprofit<i></i></div>
    </div>
    <div class="abs copy">
      <p>Copyright 2019 Kindred Harbor Network Seniorcare Nonprofit . All Rights Reserved.</p>
      <span class="social" style="left:961px"></span>
      <span class="social" style="left:997px"></span>
      <span class="social" style="left:1033px"></span>
    </div>
  </footer>

</div>
</body>
</html>
```